Grafik für Erste-Hilfe-Kurse gesucht
Zielgruppe
Berufliche Weiterbildung und Erste Hilfe Kurse
Aufgabenstellung
Eine Grafik die für Plakate und Flyer dient. Das Bild soll zur Werbung für Erste Hilfe am Kind, also für Eltern, Großeltern usw., verwendet werden. Es soll halt auffallen

```html
<!DOCTYPE html>
<html lang="de">
<head>
<meta charset="utf-8">
<title>Kurs Erste Hilfe am Kind</title>
<link rel="stylesheet" href="https://fonts.googleapis.com/css2?family=Ubuntu:wght@300;700&display=swap">
<style>
  :root {
    --stage: #e4e5e7;
    --red: #d32d2f;
    --heart-red: #c8282d;
    --charcoal: #3b3b3d;
    --white: #ffffff;
    --photo-light: #dfe3e8;
    --photo-skin: #e9b98c;
    --photo-mat: #d63a3a;
  }
  * { margin: 0; padding: 0; box-sizing: border-box; }
  html, body { width: 1200px; height: 602px; overflow: hidden; }
  body { background: var(--stage); position: relative; font-family: "Ubuntu", sans-serif; }
  .poster { position: absolute; display: block; }
  .poster--portrait { left: 261px; top: 98px; width: 281px; height: 398px; }
  .poster--landscape { left: 705px; top: 211px; width: 398px; height: 282px; }
  .headline-light { font-family: "Ubuntu", sans-serif; font-weight: 300; fill: var(--white); }
  .headline-bold { font-family: "Ubuntu", sans-serif; font-weight: 700; fill: var(--white); letter-spacing: 2px; }
</style>
</head>
<body>

<svg class="poster poster--portrait" viewBox="0 0 375 530" aria-label="Plakat Kurs Erste Hilfe am Kind, Hochformat">
  <defs>
    <clipPath id="portrait-frame"><rect width="375" height="530"/></clipPath>
    <linearGradient id="portrait-photo-tone" x1="0" y1="0" x2="0.4" y2="1">
      <stop offset="0" stop-color="var(--photo-light)"/>
      <stop offset="0.55" stop-color="var(--photo-skin)"/>
      <stop offset="1" stop-color="var(--photo-mat)"/>
    </linearGradient>
  </defs>
  <g clip-path="url(#portrait-frame)">
    <rect class="poster-ground" width="375" height="530" fill="var(--red)"/>
    <ellipse class="charcoal-swoosh" cx="285" cy="70" rx="340" ry="265" fill="var(--charcoal)"/>
    <circle class="white-ring" cx="300" cy="135" r="255" fill="var(--white)"/>
    <circle class="photo-area" role="img" aria-label="Foto: Hände üben Herzdruckmassage an einer Babypuppe auf roter Matte" cx="325" cy="140" r="205" fill="url(#portrait-photo-tone)"/>
    <path class="faint-heart" d="M260 300 C330 240, 440 260, 420 360 L300 560 L170 540" fill="none" stroke="var(--white)" stroke-opacity="0.15" stroke-width="10"/>
    <path class="heart" d="M148 232 C120 192, 60 187, 25 207 C-15 237, -10 302, 30 352 L148 490 L266 352 C306 302, 311 237, 271 207 C236 187, 176 192, 148 232 Z" fill="var(--heart-red)" fill-opacity="0.92" stroke="var(--white)" stroke-width="4"/>
    <text class="headline-light" x="58" y="278" font-size="22">KURS</text>
    <text class="headline-bold" x="58" y="310" font-size="30">ERSTE</text>
    <text class="headline-bold" x="58" y="340" font-size="30">HILFE</text>
    <text class="headline-light" x="58" y="367" font-size="22">AM KIND</text>
    <path class="cross" d="M210 288 h18 v20 h20 v18 h-20 v20 h-18 v-20 h-20 v-18 h20 Z" fill="var(--white)"/>
  </g>
</svg>

<svg class="poster poster--landscape" viewBox="0 0 530 376" aria-label="Flyer Kurs Erste Hilfe am Kind, Querformat">
  <defs>
    <clipPath id="landscape-frame"><rect width="530" height="376"/></clipPath>
    <linearGradient id="landscape-photo-tone" x1="0" y1="0" x2="0.3" y2="1">
      <stop offset="0" stop-color="var(--photo-light)"/>
      <stop offset="0.55" stop-color="var(--photo-skin)"/>
      <stop offset="1" stop-color="var(--photo-mat)"/>
    </linearGradient>
  </defs>
  <g clip-path="url(#landscape-frame)">
    <rect class="poster-ground" width="530" height="376" fill="var(--red)"/>
    <ellipse class="charcoal-swoosh" cx="330" cy="50" rx="420" ry="235" fill="var(--charcoal)"/>
    <circle class="white-ring" cx="395" cy="100" r="190" fill="var(--white)"/>
    <circle class="photo-area" role="img" aria-label="Foto: Hände üben Herzdruckmassage an einer Babypuppe auf roter Matte" cx="410" cy="100" r="160" fill="url(#landscape-photo-tone)"/>
    <path class="faint-heart" d="M360 250 C430 200, 540 230, 520 300 L420 400" fill="none" stroke="var(--white)" stroke-opacity="0.15" stroke-width="10"/>
    <path class="heart" d="M184 110 C160 75, 105 70, 72 90 C38 115, 40 175, 75 220 L184 330 L293 220 C328 175, 330 115, 296 90 C263 70, 208 75, 184 110 Z" fill="var(--heart-red)" fill-opacity="0.92" stroke="var(--white)" stroke-width="4"/>
    <text class="headline-light" x="106" y="148" font-size="20">KURS</text>
    <text class="headline-bold" x="106" y="176" font-size="27">ERSTE</text>
    <text class="headline-bold" x="106" y="203" font-size="27">HILFE</text>
    <text class="headline-light" x="106" y="227" font-size="20">AM KIND</text>
    <path class="cross" d="M240 153 h17 v18 h18 v17 h-18 v18 h-17 v-18 h-18 v-17 h18 Z" fill="var(--white)"/>
  </g>
</svg>

</body>
</html>
```